How likely are people to engage in social distancing? We need a good illustration to show the data!

We surveyed U.S. adults March 20th - 24th, 2020 and asked how likely they were to engage in social distancing (and other COVID-19 related health behaviors). What did the survey find? Basically, most people intend to engage in social distancing behaviors (e.g., avoiding large crowds) and other behaviors that reduce the spread of COVID-19 (e.g., washing hands at least 20 seconds). When most people intend to engage in a behavior, then public health professionals try to leverage that to move more people to act.
Now we need innovative and professional images that attempt to communicate one or all of these findings. The specific findings are nicely summarized in the attached document. For example, 82% of participants intend to engage in social distancing.
What sort of visual are we looking for? Our preference is for an original illustration (or set of illustrations). Our preference is for (creative and powerful illustrations, but we are also open to the creative and well-executed infographics.
We need these images fast . We will award monetary prizes to the 3 best designs. If we like more than that, then we might purchase more (e.g., in past contests, we have purchased as many as 30 designs).
What we will need:
(1) The illustrations must be original and we will need the photoshop and/or illustrator files for all artwork.
(2) You can illustrate all of the findings or just one of them. We need creative approaches that do a lucid job of bringing the data to life. Most people intend to engage in these behaviors. How to communicate that? Corvantists and Halmerites do not differ in their intentions; how to communicate that?
(3) The illustration should say, somewhere: "Based on a survey of 400 U.S. adults conducted March 20 - 24th, 2020."

U.S. Adults

• Original illustrations based on the findings of the survey (see attached document).

```html
<!DOCTYPE html>
<html lang="en">
<head>
<meta charset="utf-8">
<title>Results from EmU's Coronavirus Survey</title>
<link rel="stylesheet" href="https://fonts.googleapis.com/css2?family=Arimo:wght@400;700&display=swap">
<style>
  :root {
    --blue: #0b78c4;
    --red: #d9262b;
    --ink: #111111;
    --white: #ffffff;
    --grid: #d9d9d9;
    --warm: #f6dcc0;
  }
  * { margin: 0; padding: 0; box-sizing: border-box; }
  html, body { width: 1200px; height: 2400px; overflow: hidden; background: var(--white); }
  body { font-family: "Arimo", Arial, sans-serif; color: var(--ink); position: relative; }

  .masthead {
    position: absolute; left: 0; top: 0; width: 1200px; height: 232px;
    background: var(--blue); color: var(--white);
    display: flex; align-items: center; justify-content: center; text-align: center;
  }
  .masthead h1 { font-size: 78px; font-weight: 700; line-height: 1.08; }

  .hero-art {
    position: absolute; left: 0; top: 232px; width: 1200px; height: 712px;
    background: radial-gradient(ellipse at 50% 50%, var(--warm) 0%, #fbeee0 40%, var(--white) 75%);
  }

  .band {
    position: absolute; left: 0; width: 1200px; background: var(--blue); color: var(--white);
    display: flex; align-items: center; justify-content: center; text-align: center; font-weight: 700;
  }
  .band--intent { top: 957px; height: 112px; font-size: 40px; line-height: 1.15; }
  .band--compare { top: 1456px; height: 112px; font-size: 52px; }
  .band--verdict { top: 2168px; height: 112px; font-size: 40px; line-height: 1.2; }

  .intent-list { position: absolute; left: 0; top: 1074px; width: 1200px; list-style: none; }
  .intent-list li {
    height: 46.6px; display: flex; align-items: center; padding-left: 58px; font-size: 31px;
  }
  .intent-list li:nth-child(odd) { background: var(--red); }

  .party-chart { position: absolute; left: 0; top: 1568px; }
  .party-chart text { font-family: "Arimo", Arial, sans-serif; }

  .credit {
    position: absolute; left: 0; top: 2280px; width: 1200px; height: 120px;
    display: flex; align-items: center; justify-content: space-between; padding: 0 48px 0 26px;
  }
  .credit p { font-size: 25px; }
  .credit .institution { display: flex; align-items: center; gap: 14px; font-size: 28px; font-weight: 700; color: var(--red); }
  .credit .institution span.mark { width: 40px; height: 40px; background: var(--red); display: inline-block; }
</style>
</head>
<body>
  <header class="masthead">
    <h1>Results from EmU's<br>Coronavirus Survey</h1>
  </header>

  <div class="hero-art" role="img" aria-label="Cartoon illustration of elephants and donkeys working from home, washing hands and keeping six feet apart"></div>

  <div class="band band--intent">Percent of Americans intending to<br>engage in social distancing</div>

  <ul class="intent-list">
    <li>Engage in social distancing: 82% intend to</li>
    <li>Work from home: 63% intend to</li>
    <li>Avoid large gatherings: 85% intend to</li>
    <li>Cancel social activities: 81% intend to</li>
    <li>Put distance between yourself and other people: 85% intend to</li>
    <li>Wash hands at least 20 seconds: 87% intend to</li>
    <li>Use hand sanitizer: 85% intend to</li>
    <li>Avoid touching your eyes, nose, and mouth: 81% intend to</li>
  </ul>

  <div class="band band--compare">Comparing Corvantists and Halmerites</div>

  <svg class="party-chart" width="1200" height="600" viewBox="0 0 1200 600" aria-label="Bar chart comparing Corvantist and Halmerite intentions">
    <!-- legend -->
    <rect x="404" y="36" width="22" height="18" fill="var(--red)"/>
    <text x="436" y="53" font-size="27" fill="#333">Corvantist</text>
    <rect x="620" y="36" width="22" height="18" fill="var(--blue)"/>
    <text x="652" y="53" font-size="27" fill="#333">Halmerite</text>

    <!-- grid -->
    <g stroke="var(--grid)" stroke-width="1.5">
      <line x1="256" y1="72" x2="256" y2="530"/>
      <line x1="474" y1="72" x2="474" y2="530"/>
      <line x1="692" y1="72" x2="692" y2="530"/>
      <line x1="910" y1="72" x2="910" y2="530"/>
      <line x1="1128" y1="72" x2="1128" y2="530"/>
    </g>

    <!-- category labels -->
    <g font-size="20" fill="#222" text-anchor="end">
      <text x="246" y="101">Engage in social</text><text x="246" y="124">distancing</text>
      <text x="246" y="168">Work from home</text>
      <text x="246" y="211">Avoid large</text><text x="246" y="234">gatherings</text>
      <text x="246" y="266">Cancel social</text><text x="246" y="289">activities</text>
      <text x="246" y="321">Put distance between</text><text x="246" y="344">yourself and other</text>
      <text x="246" y="376">Wash hands at least</text><text x="246" y="399">20 seconds</text>
      <text x="246" y="441">Use hand sanitizer</text>
      <text x="246" y="486">Avoid touching your</text><text x="246" y="509">eyes,nose and mouth</text>
    </g>

    <!-- bars -->
    <g>
      <rect x="256" y="90"  width="715" height="16" fill="var(--red)"/>
      <rect x="256" y="110" width="706" height="16" fill="var(--blue)"/>
      <rect x="256" y="145" width="523" height="16" fill="var(--red)"/>
      <rect x="256" y="165" width="567" height="16" fill="var(--blue)"/>
      <rect x="256" y="200" width="741" height="16" fill="var(--red)"/>
      <rect x="256" y="220" width="732" height="16" fill="var(--blue)"/>
      <rect x="256" y="255" width="715" height="16" fill="var(--red)"/>
      <rect x="256" y="275" width="698" height="16" fill="var(--blue)"/>
      <rect x="256" y="310" width="732" height="16" fill="var(--red)"/>
      <rect x="256" y="330" width="759" height="16" fill="var(--blue)"/>
      <rect x="256" y="365" width="759" height="16" fill="var(--red)"/>
      <rect x="256" y="385" width="767" height="16" fill="var(--blue)"/>
      <rect x="256" y="420" width="759" height="16" fill="var(--red)"/>
      <rect x="256" y="440" width="732" height="16" fill="var(--blue)"/>
      <rect x="256" y="475" width="698" height="16" fill="var(--red)"/>
      <rect x="256" y="495" width="715" height="16" fill="var(--blue)"/>
    </g>

    <!-- values -->
    <g font-size="20" fill="#333">
      <text x="1125" y="104">82%</text><text x="1125" y="124">81%</text>
      <text x="1125" y="159">60%</text><text x="1125" y="179">65%</text>
      <text x="1125" y="214">85%</text><text x="1125" y="234">84%</text>
      <text x="1125" y="269">82%</text><text x="1125" y="289">80%</text>
      <text x="1125" y="324">84%</text><text x="1125" y="344">87%</text>
      <text x="1125" y="379">87%</text><text x="1125" y="399">88%</text>
      <text x="1125" y="434">87%</text><text x="1125" y="454">84%</text>
      <text x="1125" y="489">80%</text><text x="1125" y="509">82%</text>
    </g>

    <!-- axis -->
    <g font-size="20" fill="#333" text-anchor="middle">
      <text x="256" y="560">0%</text>
      <text x="474" y="560">25%</text>
      <text x="692" y="560">50%</text>
      <text x="910" y="560">75%</text>
      <text x="1128" y="560">100%</text>
    </g>
  </svg>

  <div class="band band--verdict">What does this data show? No big differences.<br>Basically the same patterns.</div>

  <footer class="credit">
    <p>Based on a survey of 400 U.S. adults conducted March 20 - 24th, 2020</p>
    <div class="institution"><span class="mark"></span>Eastmere University</div>
  </footer>
</body>
</html>
```